Plumbing Company business card design

Create a business card for our plumbing company. Following info needs to be present

Website-rivertoptapworks.net
Email- rivertoptapworks@mailnest.net
Phone-555-314-2098
Address-4876 NW Larkspur Blvd STE K
Fairdale, Utah 50999

```html
<!DOCTYPE html>
<html lang="en">
<head>
<meta charset="utf-8">
<title>Rivertop Tapworks – Business Card</title>
<link href="https://fonts.googleapis.com/css2?family=Montserrat:wght@500;700&display=swap" rel="stylesheet">
<style>
  :root {
    --backdrop: #858585;
    --card-white: #ffffff;
    --brand-blue: #005299;
    --brand-red: #ee2b2b;
    --text-light: #ffffff;
  }
  * { margin: 0; padding: 0; box-sizing: border-box; }
  html, body { width: 1160px; height: 1200px; overflow: hidden; }
  body {
    background: var(--backdrop);
    font-family: "Montserrat", Arial, sans-serif;
    position: relative;
  }
  .card {
    position: absolute;
    left: 199px;
    width: 778px;
    height: 442px;
    overflow: hidden;
  }
  .card--front { top: 105px; background: var(--card-white); }
  .card--back { top: 634px; height: 444px; background: var(--brand-blue); }

  .brand {
    position: absolute;
    left: 0; right: 0;
    display: flex;
    flex-direction: column;
    align-items: center;
  }
  .brand__dot { border-radius: 50%; background: var(--brand-red); }
  .brand__name {
    font-weight: 700;
    color: var(--brand-red);
    letter-spacing: 0.02em;
    white-space: nowrap;
  }
  .card--front .brand { top: 50px; }
  .card--front .brand__dot { width: 96px; height: 96px; }
  .card--front .brand__name { font-size: 31px; margin-top: 34px; }

  .card--back .brand { top: 98px; }
  .card--back .brand__dot { width: 150px; height: 150px; }
  .card--back .brand__name { font-size: 45px; margin-top: 42px; }

  .rule-red {
    position: absolute; left: 0; right: 0;
    top: 254px; height: 5px;
    background: var(--brand-red);
  }
  .contact-panel {
    position: absolute; left: 0; right: 0;
    top: 263px; bottom: 0;
    background: var(--brand-blue);
    color: var(--text-light);
  }
  .contact-row {
    position: absolute; left: 0; right: 0;
    display: flex; justify-content: center; align-items: center;
    font-weight: 500;
    white-space: nowrap;
  }
  .contact-row--phone { top: 33px; font-size: 23px; }
  .contact-row--online { top: 70px; font-size: 21px; }
  .contact-item { display: flex; align-items: center; }
  .contact-item + .contact-item { margin-left: 10px; }
  .icon { width: 23px; height: 23px; margin-right: 9px; flex: none; }
  .address {
    position: absolute; left: 36px; right: 42px; top: 116px;
    display: flex; align-items: center;
    font-size: 19px; font-weight: 500; white-space: nowrap;
  }
  .address__line { flex: 1; height: 2px; background: var(--text-light); }
  .address__text { padding: 0 7px; }
</style>
</head>
<body>

<section class="card card--front">
  <div class="brand">
    <div class="brand__dot"></div>
    <div class="brand__name">RIVERTOP TAPWORKS</div>
  </div>
  <div class="rule-red"></div>
  <div class="contact-panel">
    <div class="contact-row contact-row--phone">
      <span class="contact-item">
        <svg class="icon" viewBox="0 0 24 24" aria-hidden="true">
          <circle cx="12" cy="12" r="12" fill="#ee2b2b"/>
          <path d="M6 10c0-2 3-3 6-3s6 1 6 3v1h-3V9.5h-6V11H6z" fill="#fff"/>
          <rect x="8" y="11.5" width="8" height="5.5" rx="1" fill="#fff"/>
        </svg>
        555-314-2098
      </span>
    </div>
    <div class="contact-row contact-row--online">
      <span class="contact-item">
        <svg class="icon" viewBox="0 0 24 24" aria-hidden="true">
          <circle cx="12" cy="12" r="12" fill="#ee2b2b"/>
          <rect x="5.5" y="7.5" width="13" height="9" rx="1" fill="#fff"/>
          <path d="M5.5 8l6.5 5 6.5-5" fill="none" stroke="#ee2b2b" stroke-width="1.3"/>
        </svg>
        rivertoptapworks@mailnest.net
      </span>
      <span class="contact-item">
        <svg class="icon" viewBox="0 0 24 24" aria-hidden="true">
          <circle cx="12" cy="12" r="12" fill="#ee2b2b"/>
          <circle cx="12" cy="12" r="6.5" fill="none" stroke="#fff" stroke-width="1.6"/>
          <path d="M5.5 12h13M12 5.5c-3 3.5-3 9.5 0 13M12 5.5c3 3.5 3 9.5 0 13" fill="none" stroke="#fff" stroke-width="1.2"/>
        </svg>
        www.rivertoptapworks.net
      </span>
    </div>
    <div class="address">
      <span class="address__line"></span>
      <span class="address__text">4876 NW Larkspur Blvd STE K Fairdale, Utah 50999</span>
      <span class="address__line"></span>
    </div>
  </div>
</section>

<section class="card card--back">
  <div class="brand">
    <div class="brand__dot"></div>
    <div class="brand__name">RIVERTOP TAPWORKS</div>
  </div>
</section>

</body>
</html>
```